Create New Bussiness Card For New Shoes Store

Vandrule is a store that sells a variety of skateboard shoes such as Kestro, Mollen etc. we also sell some skateboard and all skateboard accessories.
we like black and white style logo, but also like blue as well.
We are fully assembled with a deck, truck, wheels, and bearings. Add some personality to your board with a fun, graphic skateboard deck. Constructed of thick 7 ply maple,
Target Market(s)
Target audience: 12-40 year old
especially for young man
Industry/Entity Type
Industrial
Contact Information for Business Card
Name: Vandrule
Address1: 2483 Harlow Brisket Rd
City: Corvale
State: Nevaro
Zip: 50712
Country: US
Phone: 614830296
email: markolvenby@plimmail.test

```html
<!DOCTYPE html>
<html lang="en">
<head>
<meta charset="utf-8">
<title>Vandrule Business Card</title>
<link rel="stylesheet" href="https://fonts.googleapis.com/css2?family=Open+Sans:wght@300;400;600&display=swap">
<style>
  :root {
    --backdrop: #e9e5e0;
    --card-dark: #1f1e21;
    --card-mid: #3a393d;
    --facet: rgba(255, 255, 255, 0.05);
    --lilac: #c9a3d8;
    --white: #f2f2f2;
    --muted: #cfcfd2;
  }
  * { box-sizing: border-box; margin: 0; padding: 0; }
  html, body {
    width: 1200px; height: 970px; overflow: hidden;
    background: var(--backdrop);
    font-family: "Open Sans", Arial, sans-serif;
  }
  .stage {
    position: relative; width: 1200px; height: 970px;
    display: flex; justify-content: center; align-items: center; gap: 60px;
  }
  .card {
    position: relative; width: 420px; height: 720px; overflow: hidden;
    background: linear-gradient(160deg, var(--card-mid) 0%, var(--card-dark) 75%);
    box-shadow: 0 18px 40px rgba(0,0,0,0.25);
  }
  .card__facets { position: absolute; inset: 0; width: 100%; height: 100%; }
  .brand {
    position: absolute; left: 0; right: 0; top: 170px;
    display: flex; align-items: center; justify-content: center; gap: 18px;
  }
  .brand__dot {
    width: 34px; height: 34px; border-radius: 50%;
    border: 3px solid currentColor;
  }
  .brand__name { font-size: 60px; font-weight: 300; letter-spacing: 1px; }
  .card--front .brand { color: var(--lilac); }
  .card--back .brand { color: var(--white); }

  .features {
    position: absolute; left: 38px; right: 34px; bottom: 70px;
    list-style: none; font-size: 15px; line-height: 1.55;
  }
  .features li { position: relative; padding-left: 22px; margin-bottom: 4px; }
  .features li::before {
    content: ""; position: absolute; left: 2px; top: 6px;
    width: 5px; height: 9px; border: solid currentColor;
    border-width: 0 2px 2px 0; transform: rotate(45deg);
  }
  .features li:nth-child(odd) { color: var(--lilac); }
  .features li:nth-child(even) { color: var(--muted); }

  .contact {
    position: absolute; left: 0; right: 0; top: 400px;
    text-align: center; color: var(--white);
  }
  .contact__address {
    font-size: 16px; letter-spacing: 7px; text-transform: uppercase;
    line-height: 1.9; font-weight: 400;
  }
  .contact__rule {
    width: 54px; height: 4px; background: var(--white);
    margin: 20px auto 14px;
  }
  .contact__phone { font-size: 26px; color: var(--lilac); letter-spacing: 1px; }
  .contact__email { font-size: 22px; margin-top: 16px; }
</style>
</head>
<body>
<main class="stage">
  <section class="card card--front" aria-label="Card front">
    <svg class="card__facets" viewBox="0 0 420 720" aria-hidden="true">
      <polygon points="0,0 420,0 420,140 0,300" fill="var(--facet)"/>
      <polygon points="0,300 420,140 420,330 0,470" fill="var(--facet)"/>
      <polygon points="0,520 420,380 420,720 0,720" fill="rgba(255,255,255,0.03)"/>
    </svg>
    <div class="brand">
      <span class="brand__dot"></span>
      <span class="brand__name">Vandrule</span>
    </div>
    <ul class="features">
      <li>We are fully assembled with a deck, truck, wheels, and bearings.</li>
      <li>Add some personality to your board with a fun, graphic skateboard deck.</li>
      <li>Constructed of thick 7 ply maple.</li>
    </ul>
  </section>

  <section class="card card--back" aria-label="Card back">
    <svg class="card__facets" viewBox="0 0 420 720" aria-hidden="true">
      <polygon points="0,0 420,0 420,110 0,260" fill="var(--facet)"/>
      <polygon points="0,260 420,110 420,300 0,430" fill="var(--facet)"/>
      <polygon points="0,560 420,420 420,720 0,720" fill="rgba(255,255,255,0.03)"/>
    </svg>
    <div class="brand">
      <span class="brand__dot"></span>
      <span class="brand__name">Vandrule</span>
    </div>
    <div class="contact">
      <p class="contact__address">2483 Harlow Brisket Rd,<br>Corvale, Nevaro-50712, US</p>
      <div class="contact__rule"></div>
      <p class="contact__phone">614830296</p>
      <p class="contact__email">markolvenby@plimmail.test</p>
    </div>
  </section>
</main>
</body>
</html>
```